Soap box for artisan soaps, eco-look, high design

We need a soap box for our lovely artisan soaps. The box size is: 9 cm height x 6,5 cm width x 2,8 cm depth. It would be nice when there is a small window in the box so you can see the soap.

See attachment for an example soap box (upside down). Please use the same elements such as texts and industrie logos. The idea is that we have a generic design that we can custom-made for different soaps. We have 15 different soaps in total at the moment.

Target Market(s)

Middle to high income

Font styles to use
Decorative
Script

Requirements
Must have
• Dutch text:
• Etherische oliën
• Handgemaakt
• Natuurlijke ingrediënten

```html
<!DOCTYPE html>
<html lang="nl">
<head>
<meta charset="utf-8">
<title>Velmora – Zest &amp; Seed zeepdoos</title>
<link rel="stylesheet" href="https://fonts.googleapis.com/css2?family=Montserrat:wght@400;500;600&family=Playfair+Display:wght@700;900&display=swap">
<style>
  :root {
    --kraft: #c39b6c;
    --ink: #1b1712;
    --cream: #efe1c7;
    --cut: #111111;
    --fold: #e0201b;
    --paper: #ffffff;
    --serif: "Playfair Display", Georgia, serif;
    --sans: "Montserrat", Arial, sans-serif;
  }
  html, body {
    margin: 0;
    width: 1200px;
    height: 1097px;
    overflow: hidden;
    background: var(--paper);
  }
  .stage {
    position: absolute;
    left: 0; top: 0;
    width: 1500px;
    height: 1371px;
    transform: scale(0.8);
    transform-origin: 0 0;
    font-family: var(--sans);
    color: var(--ink);
  }
  .dieline { position: absolute; left: 0; top: 0; }

  .panel-rot {
    position: absolute;
    transform: rotate(90deg);
    transform-origin: 0 0;
  }
  .panel-rot > * { position: absolute; margin: 0; }

  .heading {
    font-family: var(--serif);
    font-weight: 900;
    font-size: 27px;
    line-height: 1;
  }
  .copy {
    font-size: 12.6px;
    line-height: 16.8px;
    text-align: justify;
  }
  .copy--left { text-align: left; }
  .brand-name {
    font-family: var(--sans);
    font-weight: 600;
    line-height: 1;
    white-space: nowrap;
    color: var(--ink);
  }
  .free-from {
    border: 1.2px solid var(--cream);
    box-sizing: border-box;
    text-align: center;
    padding-top: 12px;
    font-size: 13px;
    line-height: 17px;
  }
  .free-from strong {
    display: block;
    font-family: var(--serif);
    font-size: 19px;
    color: var(--cream);
    margin-bottom: 3px;
  }
  .address {
    text-align: right;
    font-size: 11px;
    line-height: 18px;
  }
  .address b { font-weight: 600; font-size: 12.5px; }
  .net-weight {
    display: flex;
    align-items: center;
    gap: 10px;
    font-family: var(--serif);
    font-weight: 900;
    font-size: 25px;
  }
  .icon-dot { width: 30px; height: 30px; border-radius: 50%; background: var(--ink); }
  .icon-ring { width: 20px; height: 20px; border-radius: 50%; border: 2px solid var(--ink); }
  .icon-square { width: 26px; height: 30px; border: 2px solid var(--ink); box-sizing: border-box; border-radius: 4px; }

  .front-name {
    position: absolute;
    left: 962px; top: 420px;
    font-size: 36px;
  }
  .front-type {
    position: absolute;
    right: 190px;
    top: 698px;
    text-align: right;
  }
  .front-type .kind {
    font-weight: 600;
    font-size: 21px;
    line-height: 24px;
  }
  .front-type .tagline {
    font-size: 16px;
    line-height: 20px;
  }
</style>
</head>
<body>
<div class="stage">

  <svg class="dieline" width="1500" height="1371" viewBox="0 0 1500 1371" xmlns="http://www.w3.org/2000/svg">
    <defs>
      <linearGradient id="soap" x1="0" y1="0" x2="1" y2="0">
        <stop offset="0" stop-color="#c99a86"/>
        <stop offset="0.25" stop-color="#c99a86"/>
        <stop offset="0.3" stop-color="#e08a2e"/>
        <stop offset="1" stop-color="#d9801f"/>
      </linearGradient>
      <linearGradient id="swirl" x1="0" y1="0" x2="1" y2="1">
        <stop offset="0" stop-color="#efe1c7" stop-opacity="0.25"/>
        <stop offset="0.5" stop-color="#efe1c7" stop-opacity="0.55"/>
        <stop offset="1" stop-color="#efe1c7" stop-opacity="0.3"/>
      </linearGradient>
    </defs>

    <rect x="28" y="28" width="1444" height="1309" fill="var(--kraft)"/>

    <path role="img" aria-label="Cream marbled swirl pattern" fill="url(#swirl)"
      d="M907,960 C1000,900 1080,820 1200,790 C1280,770 1340,770 1370,760 L1370,1200 L907,1200 Z"/>
    <path role="img" aria-label="Cream marbled swirl pattern" fill="url(#swirl)"
      d="M52,555 C90,470 170,410 247,390 L247,363 L52,363 Z"/>
    <path role="img" aria-label="Cream marbled swirl pattern" fill="url(#swirl)"
      d="M520,385 C600,372 660,366 710,364 L710,392 C650,396 580,396 520,385 Z"/>

    <rect role="img" aria-label="Window showing the citrus and seed soap bar" x="962" y="471" width="354" height="114" fill="url(#soap)"/>

    <rect role="img" aria-label="Hand-lettered product name: Zest &amp; Seed" x="960" y="600" width="352" height="95" rx="6" fill="var(--cream)" fill-opacity="0.35"/>

    <rect role="img" aria-label="Hand-lettered signature: Lotte Brandsma" x="320" y="458" width="40" height="235" rx="6" fill="var(--cream)" fill-opacity="0.35"/>

    <g fill="none" stroke="var(--cut)" stroke-width="2">
      <path d="M50,363 L65,330 L77,180 L197,180 L247,363"/>
      <path d="M50,1000 L65,1033 L77,1187 L197,1187 L247,1000"/>
      <path d="M50,363 L50,1000"/>
      <path d="M247,363 L710,363 M247,1000 L710,1000"/>
      <path d="M710,363 L760,180 L878,180 L890,330 L905,363"/>
      <path d="M710,1000 L760,1187 L878,1187 L890,1033 L905,1000"/>
      <path d="M907,363 L907,160 L948,160 L948,192 M1328,192 L1328,160 L1370,160 L1370,363"/>
      <path d="M907,160 C907,92 940,50 1010,50 L1270,50 C1340,50 1370,92 1370,160"/>
      <path d="M907,1000 L907,1203 L948,1203 L948,1171 M1328,1171 L1328,1203 L1370,1203 L1370,1000"/>
      <path d="M907,1203 C907,1271 940,1313 1010,1313 L1270,1313 C1340,1313 1370,1271 1370,1203"/>
      <path d="M1370,363 L1448,385 L1448,985 L1370,1000"/>
    </g>

    <g fill="none" stroke="var(--fold)" stroke-width="1.6">
      <path d="M50,363 L247,363 M710,363 L1370,363"/>
      <path d="M50,1000 L247,1000 M710,1000 L1370,1000"/>
      <path d="M247,363 L247,1000 M710,363 L710,1000 M907,363 L907,1000 M1370,363 L1370,1000"/>
      <path d="M948,163 L1328,163 M948,1200 L1328,1200"/>
    </g>
  </svg>

  <section class="panel-rot side-story" style="left:247px; top:363px; width:637px; height:197px;">
    <p class="copy copy--left" style="left:60px; top:46px; width:345px;">
      Essentiële oliën van Lemon creëren een levendige explosie van positieve goodness, waardoor u vrolijk wakker wordt. Poppy seeds worden toegevoegd om een beetje kracht te geven bij het exfoliëren. *Lemon helpt je in een positieve state of mind te komen, waardoor je de dag beter aan kan.
    </p>
    <div class="brand-name" style="left:436px; top:112px; font-size:40px;">Velmora</div>
  </section>

  <section class="panel-rot back-panel" style="left:710px; top:363px; width:637px; height:463px;">
    <h2 class="heading" style="left:62px; top:46px;">Onze zeep</h2>
    <p class="copy" style="left:62px; top:104px; width:278px;">
      Het geeft jouw huid een heerlijk gevoel met zachte bubbels en rijke geur! Handgemaakt in kleine batches met eerlijke ingrediënten en essentiële oliën. Elke zeep wordt alleen geproduceerd als het iets goeds voor je doet en droogt minstens zes weken voordat ze worden verpakt. Ze zien er te mooi uit om te openen, maar hoe ga je dan genieten van de heerlijke bubbels, de ongelooflijke geur en je zachte, zijdeachtige huid?
    </p>
    <div class="free-from" style="left:405px; top:45px; width:196px; height:160px;">
      <strong>Vrij van:</strong>
      SLA &amp; SLSA<br>Alcohol &amp; Parabenen<br>Sorbaten &amp; Siliconen<br>Sulfaat &amp; Conserverings<br>middelen
    </div>
    <div class="brand-name" style="left:436px; top:240px; font-size:36px;">Velmora</div>
    <div class="address" style="left:420px; top:316px; width:160px;">
      Zandhaven, Nederland<br><b>velmora.nl</b>
    </div>
    <div class="net-weight" style="left:405px; top:378px;">
      120g <span class="icon-ring"></span><span class="icon-dot"></span><span class="icon-square"></span>
    </div>
  </section>

  <section class="panel-rot side-ingredients" style="left:907px; top:363px; width:637px; height:197px;">
    <p class="copy copy--left" style="left:58px; top:52px; width:535px; line-height:19.5px;">
      <b>Ingredients:</b> Olijf olie pomace (Olea europaea), Kokosnoot olie (Cocos nucifera), Palm olie (Elaeis Guineensis Kernel Oil), Water (Aqua), Citroen Etherische Olie (Citrus limonum), maanzaad (Papaver somniferum), Ijzer oxide geel (Iron Oxide). Natuurlijke bestanddelen van Etherische Olie – Citral, Citronellol, Geraniol, Limonene, Linalool.
    </p>
  </section>

  <div class="front-name brand-name">Velmora</div>
  <div class="front-type">
    <div class="kind">ETHERISCHE ZEEP</div>
    <div class="tagline">Met liefde gemaakt</div>
  </div>

</div>
</body>
</html>
```